Modern Lawfirm Business Card Design

We're looking for a business card to incorporate the newly created logo we had made.

Ideally looking for a law firm business card demonstrating, modern, minimalist, strong/bold design.

I'm open to any design honestly, but nothing "flashy".

Target Market(s)

Immigration law, family immigration, humanitarian, general legal

Industry/Entity Type

Law Firm

Contact Information for Business Card

Please use dummy information, name, street address, city, state, phone number, email, website.

Font styles to use
Serif
Sans Serif

Requirements
Must have
• Please use dummy information, name, street address, city, state, phone number, email, website.

```html
<!DOCTYPE html>
<html lang="en">
<head>
<meta charset="utf-8">
<title>Valdera Immigration Law – Business Card</title>
<link href="https://fonts.googleapis.com/css2?family=Montserrat:wght@400;600;700&family=Lato:wght@400&display=swap" rel="stylesheet">
<style>
  :root {
    --brand-blue: #1f63a6;
    --frame-grey: #bdbdbd;
    --text-grey: #6a6a6a;
    --text-dark: #3a3a3a;
    --paper: #ffffff;
    --backdrop: #ecebe8;
  }
  * { box-sizing: border-box; margin: 0; padding: 0; }
  html, body {
    width: 1200px;
    height: 1000px;
    overflow: hidden;
    background: var(--backdrop);
  }
  .canvas {
    position: relative;
    width: 1200px;
    height: 1000px;
    display: flex;
    align-items: center;
    justify-content: center;
    gap: 60px;
  }
  .card {
    position: relative;
    width: 500px;
    height: 286px;
    box-shadow: 0 6px 18px rgba(0, 0, 0, 0.18);
  }
  .card-frame {
    position: absolute;
    inset: 20px;
    border: 6px solid;
  }
  .card--front { background: var(--paper); }
  .card--front .card-frame { border-color: var(--frame-grey); }
  .card--back { background: var(--brand-blue); }
  .card--back .card-frame { border-color: var(--paper); }

  .card-content {
    position: absolute;
    inset: 0;
    display: flex;
    flex-direction: column;
    align-items: center;
    justify-content: center;
    text-align: center;
  }
  .firm-name {
    font-family: "Montserrat", sans-serif;
    font-weight: 600;
    line-height: 1.1;
    letter-spacing: 0.06em;
    text-transform: uppercase;
  }
  .firm-name__main { display: block; }
  .firm-name__sub { display: block; letter-spacing: 0.32em; }

  .card--front .firm-name { color: var(--brand-blue); margin-bottom: 10px; }
  .card--front .firm-name__main { font-size: 30px; }
  .card--front .firm-name__sub { font-size: 9px; }

  .card--back .firm-name { color: var(--paper); }
  .card--back .firm-name__main { font-size: 44px; }
  .card--back .firm-name__sub { font-size: 12px; margin-top: 4px; }

  .person-name {
    font-family: "Montserrat", sans-serif;
    font-weight: 700;
    font-size: 17px;
    color: var(--brand-blue);
    line-height: 1.1;
  }
  .person-role {
    font-family: "Montserrat", sans-serif;
    font-weight: 400;
    font-size: 12px;
    color: var(--text-grey);
    margin-bottom: 12px;
  }
  .contact-list, .contact-address {
    font-family: "Lato", sans-serif;
    font-size: 10.5px;
    color: var(--text-dark);
    line-height: 1.3;
    font-style: normal;
  }
  .contact-list { list-style: none; margin-bottom: 8px; }
</style>
</head>
<body>
<main class="canvas">
  <section class="card card--front" aria-label="Business card front">
    <div class="card-frame"></div>
    <div class="card-content">
      <div class="firm-name">
        <span class="firm-name__main">Valdera</span>
        <span class="firm-name__sub">Immigration Law</span>
      </div>
      <p class="person-name">John Doe</p>
      <p class="person-role">Manager</p>
      <ul class="contact-list">
        <li>012 345 6789</li>
        <li>email@domain.com</li>
        <li>www.yoursite.com</li>
      </ul>
      <address class="contact-address">
        11 Burton St, PlaceName,<br>Destination 023
      </address>
    </div>
  </section>

  <section class="card card--back" aria-label="Business card back">
    <div class="card-frame"></div>
    <div class="card-content">
      <div class="firm-name">
        <span class="firm-name__main">Valdera</span>
        <span class="firm-name__sub">Immigration Law</span>
      </div>
    </div>
  </section>
</main>
</body>
</html>
```